Fun Billboard

I want a billboard with a fun picture of me (I'm attaching two options)

That will say:

#1 In Real Estate
#1 In Transparency

Marcus Thornby

Voted Corwin's Choice Realtor 2 years in a row!

Call/Text 410-555-0193

Then have my logo and the Corwin's Choice logo (attached)

and very small across the bottom:

The Lantern Group at Parkfield Real Estate, 2748 W Pellham Ave, Bel Air, MD 21014 833-555-0147

Billboard size is 14' tall by 48' wide

```html
<!DOCTYPE html>
<html lang="en">
<head>
<meta charset="utf-8">
<title>Marcus Thornby Billboard</title>
<link rel="stylesheet" href="https://fonts.googleapis.com/css2?family=Poppins:ital,wght@0,500;0,600;0,700;0,800;1,900&display=swap">
<style>
  :root {
    --navy: #1b2f5a;
    --navy-deep: #152649;
    --orange: #ec6a1c;
    --ink: #111111;
    --white: #ffffff;
    --stage: #9b9b9b;
    --badge: #2b2522;
  }
  * { margin: 0; padding: 0; box-sizing: border-box; }
  html, body { width: 991px; height: 1200px; overflow: hidden; }
  body {
    background: var(--stage);
    font-family: "Poppins", Arial, sans-serif;
    position: relative;
  }
  .billboard {
    position: absolute;
    left: 20px; top: 461px;
    width: 951px; height: 277px;
    background: var(--white);
    overflow: hidden;
    box-shadow: 0 6px 14px rgba(0,0,0,.35);
  }
  .billboard-shapes { position: absolute; inset: 0; }
  .brand {
    position: absolute; left: 22px; top: 30px; width: 140px;
    text-align: center; color: var(--navy);
    font-weight: 600; font-size: 14px; line-height: 1.2;
  }
  .brand-dot {
    display: block; width: 30px; height: 30px; border-radius: 50%;
    background: var(--navy); margin: 0 auto 8px;
  }
  .rank {
    position: absolute; left: 166px; top: 8px;
    color: var(--orange); font-weight: 700; font-size: 108px;
    line-height: 1; letter-spacing: -2px;
    transform: scaleX(.58); transform-origin: left top;
    white-space: nowrap;
  }
  .headline {
    position: absolute; left: 255px; top: 20px;
    font-weight: 800; font-size: 41px; line-height: 44px; letter-spacing: -0.5px;
    white-space: nowrap;
  }
  .headline .line-one { color: var(--ink); display: block; }
  .headline .line-two { color: var(--navy); display: block; }
  .phone-band {
    position: absolute; left: 0; top: 132px; width: 560px; height: 62px;
    background: var(--orange);
  }
  .phone-icon { position: absolute; left: 32px; top: 8px; width: 46px; height: 46px; }
  .phone-number {
    position: absolute; left: 91px; top: 1px;
    color: var(--white); font-weight: 900; font-style: italic;
    font-size: 53px; line-height: 60px; letter-spacing: 1px;
    white-space: nowrap;
  }
  .award-badge { position: absolute; left: 548px; top: 120px; width: 90px; height: 90px; }
  .info-band {
    position: absolute; left: 0; top: 198px; width: 951px; height: 79px;
    background: var(--navy);
  }
  .address {
    position: absolute; left: 46px; top: 10px; width: 192px;
    color: var(--white); font-weight: 600; font-size: 10px; line-height: 13.5px;
  }
  .pin { position: absolute; left: 28px; top: 10px; width: 12px; height: 14px; }
  .divider { position: absolute; top: 7px; width: 1px; height: 52px; background: rgba(255,255,255,.7); }
  .divider.one { left: 253px; }
  .divider.two { left: 454px; }
  .award-text {
    position: absolute; left: 276px; top: 9px;
    color: var(--white); font-weight: 600; font-size: 11px; line-height: 14px;
    text-transform: uppercase;
  }
  .award-text .highlight { color: var(--orange); font-size: 13px; display: block; margin-top: 3px; }
  .agent-name {
    position: absolute; left: 476px; top: 21px;
    color: var(--white); font-weight: 700; font-size: 20px;
  }
  .agent-photo {
    position: absolute; left: 705px; top: 18px; width: 240px; height: 259px;
    border-radius: 60px 60px 0 0;
    background: linear-gradient(180deg, #c49a84 0%, #2a2a30 30%, #2a2a30 58%, #ee92a2 80%, #dcb0d6 100%);
  }
</style>
</head>
<body>
  <section class="billboard">
    <svg class="billboard-shapes" viewBox="0 0 951 277" aria-hidden="true">
      <path d="M790 0 L951 0 L951 277 L705 277 C690 190 705 70 790 0 Z" fill="var(--navy-deep)"/>
      <path d="M772 0 C705 50 680 170 700 277" fill="none" stroke="var(--orange)" stroke-width="6"/>
    </svg>

    <div class="brand"><span class="brand-dot"></span>The Lantern Group</div>

    <div class="rank">#1</div>
    <h1 class="headline">
      <span class="line-one">IN REAL ESTATE</span>
      <span class="line-two">IN TRANSPARENCY</span>
    </h1>

    <div class="phone-band">
      <svg class="phone-icon" viewBox="0 0 46 46" aria-hidden="true">
        <circle cx="23" cy="23" r="22" fill="var(--white)"/>
        <path d="M15 13 l5 -1 l3 7 l-3 2 c1 3 4 6 7 7 l2 -3 l7 3 l-1 5 c-10 1 -21 -10 -20 -20 z" fill="none" stroke="var(--orange)" stroke-width="2" stroke-linejoin="round"/>
      </svg>
      <div class="phone-number">410-555-0193</div>
    </div>

    <svg class="award-badge" viewBox="0 0 90 90" role="img" aria-label="Award badge">
      <circle cx="45" cy="45" r="43" fill="var(--badge)"/>
      <circle cx="45" cy="45" r="35" fill="none" stroke="#d0a77a" stroke-width="1.5"/>
    </svg>

    <div class="info-band">
      <svg class="pin" viewBox="0 0 12 14" aria-hidden="true">
        <path d="M6 1 a4.5 4.5 0 0 1 4.5 4.5 c0 3 -4.5 7.5 -4.5 7.5 s-4.5 -4.5 -4.5 -7.5 A4.5 4.5 0 0 1 6 1 z" fill="none" stroke="var(--orange)" stroke-width="1.8"/>
        <circle cx="6" cy="5.5" r="1.5" fill="var(--orange)"/>
      </svg>
      <p class="address">The Lantern Group at Parkfield Real Estate, 2748 W Pellham Ave, Bel Air, MD 21014 833-555-0147</p>
      <span class="divider one"></span>
      <p class="award-text">Voted Corwin's Choice<br>Realtor<span class="highlight">2 Years in a row!</span></p>
      <span class="divider two"></span>
      <p class="agent-name">Marcus Thornby</p>
    </div>

    <div class="agent-photo" role="img" aria-label="Photo of Marcus Thornby in a dark suit, arms open, wearing a pink flamingo pool float"></div>
  </section>
</body>
</html>
```